New website design for tech company

I want to redesign the current website - https://lumarekin.co/
I want it to keep the same colors/branding but I want it to resemble the look and feel of the following sites
https://www.qorvanusa.com/
https://www.pradix.com/
https://www.jumplow.com/global/us/home
https://www.kettonplc.co.uk/

The site layout

Target Market(s)

tech companies

Industry/Entity Type

tech

Number of Pages Required

2 page

Font styles to use
Serif

Colors

Designer to choose colors to be used in the design.

Requirements
Must have
• a nice updated design that looks cutting edge and innovative and the site colors can match the current logo

```html
<!DOCTYPE html>
<html lang="en">
<head>
<meta charset="UTF-8">
<title>Lumarekin – Accessible Web Technology</title>
<link href="https://fonts.googleapis.com/css2?family=Montserrat:wght@400;500;600;700&family=Nunito+Sans:wght@400;600;700&display=swap" rel="stylesheet">
<style>
:root{
  --nav:#0a9776;
  --navy:#071a2e;
  --navy-2:#0c2c47;
  --green:#3db54a;
  --teal:#0b7a7f;
  --teal-2:#0a8484;
  --lime:#8dc63f;
  --mint:#eaf6d8;
  --blue:#1e9be9;
  --stat-blue:#1a86e0;
  --ink:#1f2d3a;
  --muted:#8a94a0;
  --quote:#16304f;
  --accent:#d7e05a;
  --btn-green:#5cb030;
}
*{margin:0;padding:0;box-sizing:border-box}
html,body{width:1200px;height:4258px;overflow:hidden}
body{font-family:"Nunito Sans",sans-serif;color:var(--ink);position:relative;background:var(--mint)}
.abs{position:absolute}
section,header,footer{position:absolute;left:0;width:1200px}
h1,h2,h3,.head{font-family:"Montserrat",sans-serif}

/* nav */
.site-nav{top:0;height:74px;background:var(--nav)}
.brand{left:78px;top:22px;display:flex;align-items:center;gap:8px;font-family:"Montserrat",sans-serif;font-weight:700;font-size:20px;color:var(--accent);letter-spacing:1px}
.brand i{width:14px;height:14px;border-radius:50%;background:var(--accent);display:block}
.nav-links a{position:absolute;top:30px;font-size:14px;color:#fff;text-decoration:none}
.nav-links a.active{color:var(--accent);border-bottom:1px solid var(--accent);padding-bottom:4px}

/* hero */
.hero{top:74px;height:493px;background:radial-gradient(ellipse at 45% 55%,#143a4e 0%,#0a2236 45%,#050f1f 100%)}
.hero h1{position:absolute;top:106px;width:100%;text-align:center;color:#fff;font-weight:500;font-size:41px;line-height:53px}
.hero .sub{position:absolute;top:286px;width:100%;text-align:center;color:#fff;font-size:18px}
.btn{position:absolute;display:flex;align-items:center;justify-content:center;font-family:"Montserrat",sans-serif;font-weight:600;font-size:10px;letter-spacing:.5px}
.btn-quote{left:468px;top:369px;width:112px;height:40px;background:var(--btn-green);color:#f1f5c8}
.btn-more{left:587px;top:369px;width:111px;height:40px;border:1.5px solid #fff;color:#fff}

/* about */
.about{top:567px;height:575px;background:var(--teal-2)}
.about .left{left:0;top:0;width:575px;height:363px;background:var(--green)}
.about .right{left:575px;top:0;width:625px;height:363px;background:var(--teal)}
.about-photo{left:202px;top:84px;width:322px;height:394px;background:linear-gradient(160deg,#f4d81c 0%,#f0c419 40%,#3f7fb0 75%,#d9d9d0 100%)}
.photo-bar{left:194px;top:316px;width:5px;height:162px;background:#1e88e5}
.stats{left:293px;top:433px;width:329px;height:83px;background:#fff;border-radius:6px;display:flex;justify-content:space-around;align-items:center;box-shadow:0 6px 18px rgba(0,0,0,.12)}
.stat{text-align:center}
.stat b{display:block;font-family:"Montserrat",sans-serif;font-size:20px;color:var(--stat-blue)}
.stat span{font-size:10px;color:#333}
.about .eyebrow{left:628px;top:60px;font-size:10px;color:#fff;letter-spacing:.5px}
.about h2{position:absolute;left:628px;font-size:24px;font-weight:500;color:#fff}
.about p{position:absolute;font-size:14px;line-height:24px;color:#d9efec;text-align:justify}

/* team */
.team{top:1142px;height:518px;background:var(--mint)}
.section-title{position:absolute;width:100%;text-align:center;font-family:"Montserrat",sans-serif;font-size:24px;font-weight:600;color:#2a3b4c}
.ul-blue{color:#2a3b4c;border-bottom:2px solid var(--blue);font-weight:500}
.member{position:absolute;top:162px;width:193px;height:290px;background:#fff;box-shadow:0 2px 6px rgba(0,0,0,.06)}
.member .photo{height:200px;background:linear-gradient(180deg,#e9eef0,#c9d3d8)}
.member h3{font-size:12px;font-weight:600;margin:14px 14px 4px}
.member .role{font-size:9px;margin:0 14px 8px;color:#555}
.member p{font-size:9px;line-height:14px;margin:0 14px;color:#9aa2aa}

/* services */
.services{top:1660px;height:514px;background:var(--lime)}
.services .tagline{position:absolute;top:112px;width:100%;text-align:center;font-family:"Montserrat",sans-serif;font-size:22px;color:#e8f5d0}
.service{position:absolute;top:216px;width:270px;text-align:center}
.service .icon{width:64px;height:64px;border-radius:10px;margin:0 auto 20px;display:flex;align-items:center;justify-content:center}
.service h3{font-size:15px;font-weight:600;margin-bottom:12px;color:#1f2d3a}
.service p{font-size:10px;line-height:17px;color:#fff}

/* lab */
.lab{top:2174px;height:575px;background:radial-gradient(ellipse at 55% 70%,#16465a 0%,#0a2338 45%,#040d1c 100%)}
.lab .eyebrow{left:140px;top:162px;font-family:"Montserrat",sans-serif;font-size:26px;font-weight:600;color:var(--blue)}
.lab h2{position:absolute;left:140px;top:202px;font-size:19px;font-weight:600;color:#fff;line-height:28px}
.lab h2 u{text-decoration-color:var(--blue);font-weight:500}
.lab p{position:absolute;left:140px;top:268px;width:270px;font-size:10px;line-height:17px;color:#dfe6ee}
.arrow{position:absolute;top:360px;width:40px;height:40px;border-radius:50%;display:flex;align-items:center;justify-content:center}
.lab-shots{left:445px;top:124px;width:443px;height:327px;background:linear-gradient(135deg,#4a4e7a 0%,#3a3e66 55%,#2f3356 100%)}
.project-card{left:702px;top:170px;width:363px;height:264px;background:rgba(255,255,255,.94);padding:40px 38px}
.project-card .kicker{font-size:10px;color:var(--blue)}
.project-card h3{font-size:28px;line-height:32px;color:#222;font-weight:600;margin:4px 0 10px}
.project-card h3 em{font-style:normal;background:var(--blue);color:#fff;font-size:9px;padding:2px 6px;vertical-align:middle;margin-left:6px}
.project-card p{font-size:9px;line-height:13px;color:#333;width:270px}
.project-card .cta{margin-top:16px;width:142px;height:40px;background:var(--blue);color:#fff;display:flex;align-items:center;justify-content:center;font-size:15px}

/* partners */
.partners{top:2749px;height:102px;background:#eeeeee}
.partner{position:absolute;top:38px;font-family:"Montserrat",sans-serif;font-size:22px;font-weight:600;color:#7c8791;transform:translateX(-50%);display:flex;align-items:center;gap:8px}
.partner i{display:block;width:14px;height:14px;background:#9aa4ad}

/* recruit */
.recruit{top:2851px;height:227px;background:var(--lime)}
.recruit .sub{position:absolute;top:114px;width:100%;text-align:center;font-size:10px;color:#fff}
.apply{left:524px;top:136px;width:99px;height:30px;background:#2f3e54;color:#fff;font-size:10px;border-radius:2px;display:flex;align-items:center;justify-content:center}

/* testimonials */
.testimonials{top:3078px;left:66px!important;width:1063px!important;height:369px;background:var(--quote)}
.testimonials .eyebrow{position:absolute;top:63px;width:100%;text-align:center;font-size:10px;color:#fff;letter-spacing:.5px}
.testimonials h2{position:absolute;top:82px;width:100%;text-align:center;font-size:24px;font-weight:500;color:#fff}
.testimonials h2 span{color:var(--blue);border-bottom:2px solid #fff}
.quote{position:absolute;top:142px;width:395px;height:146px;background:#fff;padding:32px 28px 0 72px}
.quote .avatar{position:absolute;left:28px;top:32px;width:30px;height:30px;border-radius:50%;background:linear-gradient(#d8dde2,#aab3bb)}
.quote h4{font-size:10px;font-weight:700}
.stars{color:#f5c518;font-size:12px;letter-spacing:3px;margin:2px 0 8px}
.quote p{font-size:10px;line-height:16px;color:#333;margin-left:-28px}
.dots{position:absolute;top:306px;left:0;width:100%;display:flex;justify-content:center;gap:5px}
.dots i{width:4px;height:4px;border-radius:50%;background:#fff;opacity:.9}
.dots i:first-child{opacity:.4}

/* contact */
.contact{top:3488px;left:175px!important;width:833px!important;height:535px;background:#fff}
.contact h2{position:absolute;left:75px;top:52px;font-size:30px;line-height:41px;font-weight:600;color:#333}
.contact .lead{position:absolute;left:75px;top:190px;font-size:11px;line-height:20px;color:#b3b9bf;width:270px}
.ci{position:absolute;left:80px;display:flex;gap:14px;align-items:flex-start}
.ci b{display:block;font-size:14px;font-weight:600;color:#333}
.ci span{font-size:11px;color:#b3b9bf}
.field-label{position:absolute;left:423px;font-size:11px;color:#444}
.field{position:absolute;left:423px;width:330px;height:34px;display:flex;align-items:center;gap:16px;padding-left:12px;font-size:10px;color:#b8bec4}
.send{left:423px;top:430px;width:114px;height:38px;background:#14304d;color:#fff;font-size:12px;display:flex;align-items:center;justify-content:center;border-radius:3px}

/* footer */
.site-footer{top:4063px;height:195px;background:#102a48}
.site-footer .brand{left:198px;top:60px;font-size:17px}
.foot-about{left:194px;top:91px;width:180px;font-size:10px;line-height:16px;color:#dbe3ec}
.foot-col h5{font-size:10px;font-weight:700;color:#fff;margin-bottom:18px}
.foot-col a,.foot-col div{display:block;font-size:10px;color:#dbe3ec;margin-bottom:9px;text-decoration:none}
.foot-col .row{display:flex;gap:10px;align-items:flex-start}
.sub-input{left:815px;top:83px;width:187px;height:33px;background:#2b4463;color:#dbe3ec;font-size:10px;display:flex;align-items:center;padding-left:10px}
.sub-btn{left:815px;top:129px;width:187px;height:33px;background:var(--blue);color:#fff;font-size:10px;font-weight:700;display:flex;align-items:center;justify-content:center}
</style>
</head>
<body>

<header class="site-nav">
  <div class="abs brand"><i></i>LUMAREKIN</div>
  <nav class="nav-links">
    <a href="#" class="active" style="left:552px">Home</a>
    <a href="#" style="left:623px">Services</a>
    <a href="#" style="left:712px">The lab</a>
    <a href="#" style="left:795px">About us</a>
    <a href="#" style="left:889px">Partners</a>
    <a href="#" style="left:983px">Contact us</a>
  </nav>
</header>

<section class="hero" role="img" aria-label="Dark technology background with glowing network lines">
  <h1>Our Vision Is To Provide<br>Ubiquitous ADA Compliant Web<br>Technologies To Shift</h1>
  <div class="sub">Lumarekin - A subsidiary of Orvell &amp; Co.</div>
  <div class="btn btn-quote">GET A QUOTE</div>
  <div class="btn btn-more">LEARN MORE</div>
</section>

<section class="about">
  <div class="abs left"></div>
  <div class="abs right"></div>
  <div class="abs photo-bar"></div>
  <div class="abs about-photo" role="img" aria-label="Colleagues working together at computers in a bright office"></div>
  <div class="abs stats">
    <div class="stat"><b>200+</b><span>Team member</span></div>
    <div class="stat"><b>900+</b><span>Client review</span></div>
    <div class="stat"><b>20+</b><span>Complete project</span></div>
  </div>
  <div class="abs eyebrow">ABOUT US</div>
  <h2 style="top:122px">What is Lumarekin?</h2>
  <p style="left:628px;top:167px;width:440px">Lumarekin is a web based Internet and technology agency aimed at serving, educating, and partnering with brands &amp; organizations on how their products and services can advance the disabled community through inclusion and diversity. By integrating strategies, solutions, and practices accommodating all persons, we strive to shift humanity forward with the power of technology.</p>
  <h2 style="top:394px">Mission Statement</h2>
  <p style="left:664px;top:441px;width:438px">To increase awareness and opportunities in the personal &amp; professional lives of disabled persons through technology, regardless of gender, age race or socio-economic background.</p>
</section>

<section class="team">
  <h2 class="section-title" style="top:66px">Experience &amp; Our <span class="ul-blue">Professionals Team</span></h2>
  <div class="member" style="left:177px">
    <div class="photo" role="img" aria-label="Portrait of the chief operating officer"></div>
    <h3>Tarek Alvani</h3><div class="role">COO</div>
    <p>Lorem ipsum dolor sit amet consectetur. Lectus vitae ipsum quam fames</p>
  </div>
  <div class="member" style="left:497px">
    <div class="photo" role="img" aria-label="Portrait of the chief executive officer"></div>
    <h3>Jon Perella</h3><div class="role">CEO</div>
    <p>Lorem ipsum dolor sit amet consectetur. Lectus vitae ipsum quam fames</p>
  </div>
  <div class="member" style="left:810px">
    <div class="photo" role="img" aria-label="Portrait of a company officer"></div>
    <h3>Soren Abadi</h3><div class="role">CO</div>
    <p>Lorem ipsum dolor sit amet consectetur. Lectus vitae ipsum quam fames</p>
  </div>
</section>

<section class="services">
  <h2 class="section-title" style="top:76px;color:#1f2d3a"><span style="border-bottom:2px solid var(--blue)">That Is The Best Service</span></h2>
  <div class="tagline">Determine The Service You Need</div>
  <div class="service" style="left:136px">
    <div class="icon" style="background:#fbd24e"><svg width="28" height="28" viewBox="0 0 24 24" fill="none" stroke="#fff" stroke-width="1.6"><rect x="3" y="5" width="18" height="14" rx="2"/><path d="M3 9h18M9 13l-2 2 2 2M15 13l2 2-2 2"/></svg></div>
    <h3>Web &amp; Digital Accessibility</h3>
    <p>Lorem ipsum dolor sit amet consectetur. Lectus vitae ipsum quam fames rhoncus cras leo a dictum. Tristique habitant orci arcu et.</p>
  </div>
  <div class="service" style="left:445px">
    <div class="icon" style="background:#3fd8e0"><svg width="28" height="28" viewBox="0 0 24 24" fill="none" stroke="#fff" stroke-width="1.6"><path d="M12 3l9 5-9 5-9-5 9-5z"/><path d="M3 12l9 5 9-5M3 16l9 5 9-5"/></svg></div>
    <h3>Training &amp; Education</h3>
    <p>Lorem ipsum dolor sit amet consectetur. Lectus vitae ipsum quam fames rhoncus cras leo a dictum. Tristique habitant orci arcu et.</p>
  </div>
  <div class="service" style="left:754px">
    <div class="icon" style="background:#1e88e5"><svg width="28" height="28" viewBox="0 0 24 24" fill="none" stroke="#fff" stroke-width="1.6"><path d="M4 8V5a1 1 0 0 1 1-1h3M16 4h3a1 1 0 0 1 1 1v3M20 16v3a1 1 0 0 1-1 1h-3M8 20H5a1 1 0 0 1-1-1v-3"/><path d="M10 9l-3 3 3 3M14 9l3 3-3 3"/></svg></div>
    <h3>Software Development</h3>
    <p>Lorem ipsum dolor sit amet consectetur. Lectus vitae ipsum quam fames rhoncus cras leo a dictum. Tristique habitant orci arcu et.</p>
  </div>
</section>

<section class="lab" role="region" aria-label="The Lab">
  <div class="abs eyebrow">The Lab</div>
  <h2>We Have Done Lot's Of<br><u>Project</u></h2>
  <p>Lorem ipsum dolor sit amet consectetur. Lectus vitae ipsum quam fames rhoncus cras leo a dictum. Tristique habitant orci arcu et.</p>
  <div class="arrow" style="left:140px;background:#2a3444"><svg width="14" height="14" viewBox="0 0 24 24" fill="none" stroke="#7fa0c0" stroke-width="2"><path d="M19 12H5M11 6l-6 6 6 6"/></svg></div>
  <div class="arrow" style="left:196px;background:var(--blue)"><svg width="14" height="14" viewBox="0 0 24 24" fill="none" stroke="#fff" stroke-width="2"><path d="M5 12h14M13 6l6 6-6 6"/></svg></div>
  <div class="abs lab-shots" role="img" aria-label="Fitness app screens shown on phone mockups"></div>
  <div class="abs project-card">
    <div class="kicker">Happy Clint</div>
    <h3>Apps development Project<em>★ 5</em></h3>
    <p>Lorem ipsum dolor sit amet consectetur. Ut fringilla iaculis donec quis congue consectetur dui in. Malesuada mattis sed neque euismod hendrerit. Ac felis quam tincidunt egestas ipsum in.</p>
    <div class="cta">Learn more</div>
  </div>
</section>

<section class="partners">
  <div class="partner" style="left:310px">Quillon</div>
  <div class="partner" style="left:490px;font-size:17px;font-weight:500"><i></i>Brevanta</div>
  <div class="partner" style="left:678px">Payvora</div>
  <div class="partner" style="left:863px">Stitchly</div>
</section>

<section class="recruit">
  <h2 class="section-title" style="top:62px">Recruitment for Partnerships</h2>
  <div class="sub">Join us as a Partner and unlock a world of opportunities.</div>
  <div class="abs apply">Apply Now</div>
</section>

<section class="testimonials">
  <div class="eyebrow">CLIENT TESTOMONIAL</div>
  <h2>What Our <span>Clients Say</span>?</h2>
  <div class="quote" style="left:127px">
    <div class="avatar"></div>
    <h4>Milo Danvers</h4><div class="stars">★★★★★</div>
    <p>Lorem ipsum dolor sit amet consectetur. Ullamcorper egestas aliquam commodo faucibus cursus augue. Scelerisque facilisis sit ac enim mauris sed vel ipsum morbi.</p>
  </div>
  <div class="quote" style="left:541px">
    <div class="avatar"></div>
    <h4>Milo Danvers</h4><div class="stars">★★★★★</div>
    <p>Lorem ipsum dolor sit amet consectetur. Ullamcorper egestas aliquam commodo faucibus cursus augue. Scelerisque facilisis sit ac enim mauris sed vel ipsum morbi.</p>
  </div>
  <div class="dots"><i></i><i></i><i></i><i></i><i></i></div>
</section>

<section class="contact">
  <h2>Lets talk with<br>our awesome<br>team</h2>
  <div class="lead">Our mission is to help your business grow, especially financially. You can consult anytime</div>
  <div class="ci" style="top:266px">
    <svg width="28" height="28" viewBox="0 0 24 24" fill="none" stroke="#333" stroke-width="1.3"><path d="M5 4h4l2 5-2.5 1.5a11 11 0 0 0 5 5L15 13l5 2v4a2 2 0 0 1-2 2A16 16 0 0 1 3 6a2 2 0 0 1 2-2z"/></svg>
    <div><b>Call</b><span>08452 600 118</span></div>
  </div>
  <div class="ci" style="top:330px">
    <svg width="28" height="28" viewBox="0 0 24 24" fill="none" stroke="#333" stroke-width="1.3"><rect x="3" y="6" width="18" height="13" rx="1"/><path d="M3 7l9 7 9-7"/></svg>
    <div><b>Email</b><span>hello@lumarekin.co</span></div>
  </div>
  <div class="ci" style="top:394px">
    <svg width="28" height="28" viewBox="0 0 24 24" fill="none" stroke="#333" stroke-width="1.3"><path d="M3 6l6-2 6 2 6-2v14l-6 2-6-2-6 2z"/><circle cx="12" cy="10" r="2"/></svg>
    <div><b>Location</b><span>Brookvale, Texas</span></div>
  </div>
  <div class="field-label" style="top:96px">Your name</div>
  <div class="field" style="top:123px"><svg width="12" height="12" viewBox="0 0 24 24" fill="none" stroke="#777" stroke-width="2"><circle cx="12" cy="8" r="4"/><path d="M4 21c1-5 15-5 16 0"/></svg>Full name here</div>
  <div class="field-label" style="top:184px">Your mail</div>
  <div class="field" style="top:206px"><svg width="12" height="12" viewBox="0 0 24 24" fill="none" stroke="#777" stroke-width="2"><rect x="3" y="6" width="18" height="13"/><path d="M3 7l9 7 9-7"/></svg>Your email address</div>
  <div class="field-label" style="top:273px">Message</div>
  <div class="field" style="top:303px">Type your message here</div>
  <div class="abs send">Send message</div>
</section>

<footer class="site-footer">
  <div class="abs brand"><i></i>LUMAREKIN</div>
  <div class="abs foot-about">Lorem Ipsum is simply dummy text of the print ing landtypesetting indust Lorem Ipsum has been the industry's standard dummy text .</div>
  <div class="abs foot-col" style="left:445px;top:44px">
    <h5>QUICK LINK</h5>
    <a href="#">Home</a><a href="#">Services</a><a href="#">Pages</a><a href="#">About Us</a>
  </div>
  <div class="abs foot-col" style="left:585px;top:44px">
    <h5>GET IN TOUCH</h5>
    <div class="row"><svg width="9" height="11" viewBox="0 0 24 24" fill="var(--blue)"><path d="M12 2a7 7 0 0 0-7 7c0 5 7 13 7 13s7-8 7-13a7 7 0 0 0-7-7z"/></svg><span>Harbor Lane, USA<br>1212 Westfield-3500</span></div>
    <div class="row"><svg width="9" height="11" viewBox="0 0 24 24" fill="var(--blue)"><path d="M5 3h4l2 5-2.5 1.5a11 11 0 0 0 5 5L15 12l5 2v4a2 2 0 0 1-2 2A16 16 0 0 1 3 5a2 2 0 0 1 2-2z"/></svg><span>123 555 0190</span></div>
    <div class="row"><svg width="9" height="11" viewBox="0 0 24 24" fill="var(--blue)"><path d="M2 5h20v14H2z"/></svg><span>info@lumarekin.co</span></div>
  </div>
  <div class="abs foot-col" style="left:815px;top:44px"><h5>SUBSCRIBE TO NEWS</h5></div>
  <div class="abs sub-input">Your Email</div>
  <div class="abs sub-btn">SUBSCRIBE NOW</div>
</footer>

</body>
</html>
```